Website concept design - need very creative and polished web page layouts

Need 3-4 web pages designed (graphic only). Client is an interior designer and has specific design requirements. Need a skilled graphic designer to help me create a concept for the new site.

The site is primarily meant to allow users to build and buy a new product, but should have a portfolio site feel. I have specific requirements so designer won't have to 'figure it out' on their own.

Making use of white space, text orientation, and object movement are essential to the success of this project.

Inspirational sites:

http://brisk.tamo.site/#en - creative and atypical
https://pembly.io/ - white space and movement; vertical menu links
https://738q.jp- modern into, object hover movement
https://www.polnaxo.com/case-copper-reed - white space, dimensional feel of objects floating on page; pop of color

Target Market(s)

Interior designers and individuals - both commercial and retail.

Industry/Entity Type

Interior Design

Number of Pages Required

4 page

Font styles to use
Serif
Sans Serif

Requirements
Must have
• Professional design, meet design requirements, professional and highly creative look. This cannot look like or resemble in any way a common or typical website. Making use of white space, text orientation, and object movement are essential to the success of this project.
• Colors for the project:
• COLOR TREATMENT - (Not Final)
• DARK PUTTY – 77% Black
• R 95
• G 96
• B 98
• LIGHT PUTTY – 50% Black
• R 129
• G 131
• B 134
• ** Other Levels of Putty can be used.
• BLUE GREEN - (May not be final)
• R 113
• G 202
• B 210
Should not have
• Cannot look like or resemble a typical website design.

```html
<!DOCTYPE html>
<html lang="en">
<head>
<meta charset="utf-8">
<title>Lumera — Lamps</title>
<link href="https://fonts.googleapis.com/css2?family=Open+Sans:wght@300;400;600;700&display=swap" rel="stylesheet">
<style>
:root{
  --teal:#71cad2;
  --ink:#333436;
  --putty-dark:#5f6062;
  --putty-light:#818386;
  --band:#f5f5f5;
  --foot:#f3f3f3;
  --white:#ffffff;
  --line:#c9c9c9;
}
*{margin:0;padding:0;box-sizing:border-box}
html,body{width:1200px;height:3681px;overflow:hidden}
body{position:relative;background:var(--white);font-family:"Open Sans",Arial,sans-serif;color:var(--ink)}
.abs{position:absolute}
section{position:absolute;left:0;width:1200px;overflow:hidden}

/* hero menu */
.hero{top:0;height:609px;background:linear-gradient(180deg,#ffffff 0%,#f8f9f9 60%,#f1f2f2 100%)}
.close-btn{left:84px;top:10px;width:50px;height:50px}
.logo{left:0;width:1200px;top:28px;text-align:center;font-weight:300;font-size:26px;letter-spacing:2px;color:var(--putty-dark)}
.hero-bg-word{left:0;width:1200px;top:262px;text-align:center;font-size:78px;font-weight:700;letter-spacing:4px;color:#eef0f0}
.menu{left:0;width:1200px;top:96px;list-style:none;text-align:center}
.menu li{height:88.3px;font-size:23px;color:#222;font-weight:400;line-height:36px}

/* shared */
.title{left:0;width:1200px;text-align:center;font-weight:300;font-size:39px;letter-spacing:1px;color:var(--ink)}
.wave{width:84px;height:14px}
.body-copy{font-size:13px;line-height:21px;color:var(--putty-dark);text-align:center}

/* about */
.about{top:609px;height:618px;background:var(--band)}
.about .title{width:766px;top:128px}
.about .wave{left:341px;top:190px}
.about .body-copy{left:120px;width:526px;top:248px}
.btn{left:304px;top:466px;width:150px;height:32px;background:var(--teal);color:#fff;font-size:13px;text-align:center;line-height:32px}
.about-lamp{left:687px;top:103px;width:466px;height:515px;border-radius:48% 48% 8% 8%/42% 42% 8% 8%;background:linear-gradient(180deg,#8a5a1c 0%,#e9b63c 25%,#f3d77e 45%,#6b4a35 70%,#3b2d26 100%)}

/* customise */
.customize{top:1227px;height:785px;background:var(--white)}
.customize .title{top:103px}
.customize .wave{left:558px;top:179px}
.room-photo{left:0;top:196px;width:405px;height:589px;background:linear-gradient(90deg,#f7f2ea 0%,#fbf8f3 60%,rgba(255,255,255,0) 100%)}
.builder{left:437px;top:245px;width:326px;height:258px;box-shadow:0 10px 24px rgba(0,0,0,.18);background:radial-gradient(ellipse at 50% 45%,#fbfbfb 0%,#f1eeed 45%,#ececec 75%),#ececec}
.builder-base{left:535px;top:425px;width:130px;height:70px;border-radius:50%;background:radial-gradient(ellipse at 50% 50%,rgba(233,81,60,.35) 0%,rgba(233,81,60,0) 70%)}
.chev{left:585px;top:548px;width:30px;height:24px}
.select-label{left:0;width:1200px;top:592px;text-align:center;font-size:14px;letter-spacing:2px;font-weight:600;color:var(--putty-dark)}

/* collections */
.collections{top:2012px;height:700px;background:var(--band)}
.collections .title{top:85px}
.collections .wave{left:558px;top:144px}
.tile{top:214px;width:238px;height:395px}
.tile-1{left:86px;background:linear-gradient(160deg,#d9c9ac,#7a6a52 80%)}
.tile-2{left:351px;background:linear-gradient(150deg,#b64a6a 0%,#efe4d5 45%,#d7c4a6 100%)}
.tile-3{left:614px;background:linear-gradient(170deg,#f1e0cf 0%,#e9a78a 40%,#f6efe7 100%)}
.tile-4{left:879px;background:linear-gradient(170deg,#5a6163,#3f4546 70%,#2f3233)}
.tile-4 .view{position:absolute;left:0;right:0;top:182px;text-align:center;color:#fff;font-weight:700;font-size:19px;letter-spacing:.5px}

/* testimonial */
.testimonial{top:2712px;height:540px;background:var(--white)}
.test-lamp{left:74px;top:49px;width:490px;height:491px;background:linear-gradient(180deg,#2e3445 0%,#3a4054 45%,#b9b3a8 62%,#cfc9bf 85%,#9b8a72 100%)}
.testimonial .title{left:630px;width:380px;top:92px;font-size:35px}
.testimonial .wave{left:778px;top:143px}
.quote-mark{left:802px;top:185px;width:34px;height:24px}
.testimonial .body-copy{left:600px;width:440px;top:240px}
.author{left:600px;width:440px;top:322px;text-align:center;font-weight:700;font-size:15px}
.dots{left:793px;top:394px;display:flex;gap:6px}
.dots span{width:12px;height:12px;background:#d4d4d4}
.dots span.on{background:#fff;border:1px solid #bbb}

/* footer */
.footer{top:3252px;height:368px;background:var(--foot)}
.col-head{top:112px;font-size:21px;font-weight:300;color:var(--ink)}
.col-rule{height:1px;background:var(--line);width:238px}
.links{left:86px;top:164px;list-style:none}
.links li{height:35.6px;font-size:14px;color:#444;display:flex;align-items:center;gap:14px}
.links li i{width:12px;height:12px;border-radius:50%;background:var(--teal);display:inline-block}
.email-field{left:437px;top:171px;width:160px;height:35px;background:#fff;border:1px solid #ddd;font-size:10px;color:#999;padding-left:12px;line-height:33px}
.signup{left:597px;top:171px;width:74px;height:35px;background:var(--teal);color:#fff;font-size:12px;font-weight:600;line-height:35px;text-align:center}
.socials{left:437px;top:290px;display:flex;gap:21px}
.socials span{width:33px;height:33px;border-radius:50%;display:block}
.contact-row{left:788px;display:flex;gap:18px;font-size:13px;color:#444;line-height:20px;width:330px}
.contact-row svg{flex:0 0 14px;margin-top:3px}
.copyright{left:0;top:3620px;width:1200px;height:61px;background:var(--teal);color:#fff;text-align:center;font-size:12px;letter-spacing:1.5px;line-height:61px}
</style>
</head>
<body>

<section class="hero">
  <svg class="abs close-btn" viewBox="0 0 50 50"><circle cx="25" cy="25" r="23" fill="none" stroke="var(--teal)" stroke-width="2.5"/><path d="M15 15L35 35M35 15L15 35" stroke="var(--teal)" stroke-width="2.5"/></svg>
  <div class="abs logo">LUMERA</div>
  <div class="abs hero-bg-word">DRIVE YOUR STYLES</div>
  <ul class="abs menu">
    <li>Home</li><li>Inspiration</li><li>Color</li><li>Pattern</li><li>Contact</li>
  </ul>
</section>

<section class="about">
  <h2 class="abs title">ABOUT US</h2>
  <svg class="abs wave" viewBox="0 0 84 14"><path d="M2 7q8-8 16 0t16 0t16 0t16 0t16 0" fill="none" stroke="var(--teal)" stroke-width="3"/></svg>
  <p class="abs body-copy">Lorem Ipsum is simply dummy text of the printing and typesetting industry. Lorem Ipsum has been the industry's standard dummy text ever since the 1500s, when an unknown printer took a galley of type and scrambled it to make a type specimen book. It has survived not only.<br>Lorem Ipsum is simply dummy text of the printing and typesetting industry. Lorem Ipsum has been the industry's standard dummy text ever since the 1500s, when an unknown printer took a galley of type and scrambled it to make a type specimen book. It has survived not only.</p>
  <div class="abs btn">Read More</div>
  <div class="abs about-lamp" role="img" aria-label="Amber stained-glass table lamp with a dark bronze base"></div>
  <svg class="abs" style="left:0;top:578px" width="1200" height="40" viewBox="0 0 1200 40" preserveAspectRatio="none"><path d="M0 40V22Q600 -10 1200 22V40Z" fill="#fff"/></svg>
</section>

<section class="customize">
  <div class="abs room-photo" role="img" aria-label="Faded room scene with a cream table lamp on a white side table"></div>
  <h2 class="abs title">CUSTOMIZE&nbsp; YOUR LAMP</h2>
  <svg class="abs wave" viewBox="0 0 84 14"><path d="M2 7q8-8 16 0t16 0t16 0t16 0t16 0" fill="none" stroke="var(--teal)" stroke-width="3"/></svg>
  <div class="abs builder" role="img" aria-label="Lamp preview: white shade on a red-patterned base"></div>
  <div class="abs builder-base"></div>
  <svg class="abs chev" viewBox="0 0 30 24"><path d="M5 3L15 12L25 3M5 12L15 21L25 12" fill="none" stroke="var(--teal)" stroke-width="2.5"/></svg>
  <div class="abs select-label">SELECT A BASE</div>
  <svg class="abs" style="left:0;top:745px" width="1200" height="40" viewBox="0 0 1200 40" preserveAspectRatio="none"><path d="M0 40V18Q600 0 1200 30V40Z" fill="var(--band)"/></svg>
</section>

<section class="collections">
  <h2 class="abs title">COLLECTIONS</h2>
  <svg class="abs wave" viewBox="0 0 84 14"><path d="M2 7q8-8 16 0t16 0t16 0t16 0t16 0" fill="none" stroke="var(--teal)" stroke-width="3"/></svg>
  <div class="abs tile tile-1" role="img" aria-label="Striped armchairs beside a table lamp on a teal-draped table"></div>
  <div class="abs tile tile-2" role="img" aria-label="Cream armchair with pink curtains and a side lamp"></div>
  <div class="abs tile tile-3" role="img" aria-label="Peach patterned lamp on a white dresser"></div>
  <div class="abs tile tile-4" role="img" aria-label="Dim room with a chair and a lamp on a dark nightstand"><span class="view">View&nbsp; More ➔</span></div>
</section>

<section class="testimonial">
  <div class="abs test-lamp" role="img" aria-label="Navy drum-shade lamp with a brushed silver base on a wooden shelf"></div>
  <h2 class="abs title">TESTIMONIAL</h2>
  <svg class="abs wave" viewBox="0 0 84 14"><path d="M2 7q8-8 16 0t16 0t16 0t16 0t16 0" fill="none" stroke="var(--teal)" stroke-width="3"/></svg>
  <svg class="abs quote-mark" viewBox="0 0 34 24"><path d="M2 22V12Q2 3 12 2V7Q7 8 7 12H12V22ZM20 22V12Q20 3 30 2V7Q25 8 25 12H30V22Z" fill="var(--teal)"/></svg>
  <p class="abs body-copy">Lorem Ipsum is simply dummy text of the printing and typesetting industry. Lorem Ipsum has been the industry's standard dummy text ever since the 1500s, when an unknown.</p>
  <div class="abs author">John Doe</div>
  <div class="abs dots"><span></span><span class="on"></span><span></span></div>
  <svg class="abs" style="left:0;top:500px" width="1200" height="40" viewBox="0 0 1200 40" preserveAspectRatio="none"><path d="M0 40V30Q700 -6 1200 14V40Z" fill="var(--foot)"/></svg>
</section>

<section class="footer">
  <div class="abs col-head" style="left:86px">Quick Links</div>
  <div class="abs col-rule" style="left:86px;top:147px"></div>
  <ul class="abs links">
    <li><i></i>Home</li><li><i></i>Inspiration</li><li><i></i>Color</li><li><i></i>Pattern</li><li><i></i>Contact</li>
  </ul>

  <div class="abs col-head" style="left:437px">Newsletter Signup</div>
  <div class="abs col-rule" style="left:437px;top:147px"></div>
  <div class="abs email-field">Enter your email id</div>
  <div class="abs signup">Signup</div>
  <div class="abs col-head" style="left:437px;top:234px">Follow Us</div>
  <div class="abs col-rule" style="left:437px;top:269px"></div>
  <div class="abs socials">
    <span style="background:#5f80b9"></span><span style="background:var(--teal)"></span><span style="background:#e1553e"></span><span style="background:var(--teal)"></span>
  </div>

  <div class="abs col-head" style="left:788px">Contact Information</div>
  <div class="abs col-rule" style="left:788px;top:147px;width:325px"></div>
  <div class="abs contact-row" style="top:175px"><svg width="14" height="14" viewBox="0 0 14 14"><rect width="14" height="14" rx="2" fill="var(--teal)"/><path d="M4 3q-1 4 3 8l2-1-1-2-1 1q-2-2-2-4l1-1-1-2Z" fill="#fff"/></svg>(000) 000 -0000</div>
  <div class="abs contact-row" style="top:211px"><svg width="14" height="14" viewBox="0 0 14 14"><rect y="2" width="14" height="10" rx="1" fill="var(--teal)"/><path d="M1 3L7 8L13 3" fill="none" stroke="#fff"/></svg>hello@lumera-mail.com</div>
  <div class="abs contact-row" style="top:245px"><svg width="14" height="14" viewBox="0 0 14 14"><path d="M7 0a5 5 0 0 0-5 5c0 4 5 9 5 9s5-5 5-9a5 5 0 0 0-5-5Z" fill="var(--teal)"/><circle cx="7" cy="5" r="2" fill="#fff"/></svg><span>Lorem Ipsum is simply dummy text of the printing and typesetting industry</span></div>
</section>

<footer class="abs copyright">Copyright © 2018 Lumera Light. All Rights Reserved</footer>

</body>
</html>
```